KVR PROTECTIVE COATINGS BROCHURE

To design a 4 page A4 brochure of protective coating system for steel and concrete infrastructure with industrial , telecoms and oil & gas markets.

brochure title; Inorganic siloxane protective coatings for steel and concrete infrastructure
sub title - Non-isocyanate (NISO) Coatings
Products:
- KVR 300 1K solvent free inorganic tintable finish coat for ultra UV durability
- KVR 300 DM 1K solvent free clear coat for protection of steel and concrete substrates, anti graffiti, highly UV resistant
- KVR BASEGUARD 2K epoxy hybrid anti corrosion coating for steel
- KVR TILEMAX 1K glass flake single pack high abrasion resistant coating
- KVR DURAMETAL 1K single component siloxane zinc anti-corrosion coating
- KVR TANO 1K single component intermediate anti-corrosion coating
- KVR 470 2K two component epoxy-siloxane hybrid durable tintable top coat
- KVR DECKSHIELD 2K two component, chemical resistant, durable floor coating.
- KVR STONEWEAR 2K two component ceramically filled epoxy for high abrasion resistance.

use good clear images of markets sectors (oil&gas, Telecoms, Industrial)
use icons for low VOC, low toxicity, Green, high weathering resistance, chemical resistance, maintenance friendly, environment friendly, non-isocyanate.

Table of primers and top coats in attachment, please use images within document about tinting products

Company Info
Tel +44 (0) 1632 960518
Email sales@tq-hr.example
Address 7-8 Larkwell Meadow Trade Park, Fennick Lane, United Kingdom
web www.tq-hr.example

Target Market(s)

Protective Coatings

Requirements
Must have
• Clear images of target markets and good layout of information provided

```html
<!DOCTYPE html>
<html lang="en">
<head>
<meta charset="utf-8">
<title>KVR Protective Coatings Brochure</title>
<link rel="stylesheet" href="https://fonts.googleapis.com/css2?family=Barlow:wght@400;500;600;700&family=Oswald:wght@500;600&display=swap">
<style>
:root{
  --navy:#1d3f95;
  --deep:#17357f;
  --sky:#4a9fd8;
  --sky-light:#5aaee0;
  --ink:#1a1a1a;
  --grey-text:#5b5f66;
  --stage:#e8ecf0;
  --cell-grey:#d8d4cc;
  --cell-red:#e77a6d;
  --cell-orange:#f4a93a;
  --slate:#4d5775;
  --slate-2:#5d6785;
  --teal:#5fc0bd;
  --steel:#8a92a3;
}
*{margin:0;padding:0;box-sizing:border-box}
html,body{width:837px;height:1200px;overflow:hidden}
body{background:var(--stage);font-family:"Barlow",sans-serif;color:var(--ink);position:relative}
.page{position:absolute;left:44px;width:749px;height:528px;background:#fff;overflow:hidden;box-shadow:0 2px 10px rgba(0,0,0,.12)}
.page--cover{top:55px}
.page--inside{top:615px}
.page-art{position:absolute;inset:0}

/* cover */
.brand{position:absolute;right:25px;top:62px;display:flex;align-items:center;gap:8px;font-family:"Barlow",sans-serif;font-weight:700;font-size:24px;color:var(--navy);letter-spacing:.2px}
.brand__dot{width:16px;height:16px;border-radius:50%;background:var(--sky)}
.cover-title{position:absolute;right:25px;top:142px;text-align:right;font-family:"Oswald",sans-serif;font-weight:600;font-size:21px;line-height:22px;color:var(--navy);text-transform:uppercase}
.cover-subtitle{position:absolute;right:24px;top:240px;height:24px;line-height:24px;color:#fff;font-size:13.5px;font-weight:400}
.contact{position:absolute;right:394px;top:401px;text-align:right;font-size:12.5px;line-height:16.6px;color:var(--ink)}
.contact li{list-style:none;display:flex;justify-content:flex-end;align-items:center;gap:10px}
.contact svg{width:9px;height:9px;flex:none}
.web-bar{position:absolute;left:203px;top:481px;width:153px;height:23px;background:var(--sky-light);color:#fff;font-size:12.5px;display:flex;align-items:center;justify-content:flex-end;gap:8px;padding-right:8px}
.web-bar svg{width:9px;height:9px}

/* inside */
.products{position:absolute;left:24px;top:268px;width:320px}
.products h2{font-size:17px;font-weight:700;margin-bottom:13px}
.products li{list-style:none;font-size:6.8px;line-height:8px;position:relative;padding-left:11px;margin-bottom:6px}
.products li svg{position:absolute;left:0;top:1px;width:6px;height:6px}
.spec{position:absolute;left:396px}
.spec h3{font-size:12.5px;font-weight:700;margin-bottom:8px}
.spec--primers{top:23px}
.spec--topcoats{top:256px}
.spec-table{border-collapse:collapse;table-layout:fixed;width:329px;font-size:6.6px;text-align:center}
.spec-table th,.spec-table td{border:1px solid #6b6b6b;height:19.2px;padding:0 2px;line-height:7px}
.spec-table th{font-weight:700}
.col-product{width:75px}.col-comp{width:49px}.col-func{width:91px}.col-chem{width:68px}.col-dft{width:46px}
.spec-table--primers .c-product{background:var(--cell-grey)}
.spec-table--primers .c-comp,.spec-table--primers .c-chem{background:var(--cell-red);color:#5a1e18}
.spec-table--primers .c-func{background:var(--cell-orange);color:#5a3300}
.spec-table--primers .c-dft{background:var(--cell-grey)}
.spec-table--primers td{color:#444}
.spec-table--topcoats th,.spec-table--topcoats td{border-color:#2e344a;color:#fff}
.spec-table--topcoats .c-product{background:var(--slate)}
.spec-table--topcoats .c-comp{background:var(--slate-2)}
.spec-table--topcoats .c-func{background:var(--teal)}
.spec-table--topcoats .c-chem{background:var(--steel)}
.spec-table--topcoats .c-dft{background:var(--slate)}
.spec-table--topcoats td{color:#e7ebf3}
</style>
</head>
<body>

<section class="page page--cover">
  <svg class="page-art" viewBox="0 0 749 528" width="749" height="528">
    <defs>
      <linearGradient id="worker-tones" x1="0" y1="0" x2="1" y2="1">
        <stop offset="0" stop-color="#d9d2c4"/><stop offset=".5" stop-color="#b9a58f"/><stop offset="1" stop-color="#7e8b93"/>
      </linearGradient>
      <linearGradient id="plant-tones" x1="0" y1="0" x2="0" y2="1">
        <stop offset="0" stop-color="#2e7fc8"/><stop offset=".55" stop-color="#6f9ec4"/><stop offset="1" stop-color="#3b4a5a"/>
      </linearGradient>
    </defs>
    <path d="M0,0 H480 C445,130 335,228 175,238 C95,243 35,226 0,206 Z" fill="#4a9fd8"/>
    <path d="M0,0 H332 C330,115 255,232 140,234 C80,235 32,220 0,200 Z" fill="url(#worker-tones)" role="img" aria-label="Photo: engineer in orange overalls and hard hat at an industrial plant"/>
    <path d="M0,528 C30,400 190,262 430,248 L430,300 C235,300 82,402 24,528 Z" fill="#1d3f95"/>
    <path d="M374,302 C396,272 418,254 440,248 H749 V528 H374 Z" fill="url(#plant-tones)" role="img" aria-label="Photo: oil and gas refinery columns under a blue sky"/>
    <polygon points="488,264 520,240 749,240 749,264" fill="#4a9fd8"/>
  </svg>

  <div class="brand"><span class="brand__dot"></span>Tarquin Resins</div>

  <h1 class="cover-title">Inorganic Siloxane<br>Protective Coatings for<br>Steel and Concrete<br>Infrastructure</h1>
  <p class="cover-subtitle">Non-isocyanate (NISO) Coatings</p>

  <ul class="contact">
    <li>+44 (0) 1632 960518 <svg viewBox="0 0 10 10"><path d="M2 1l2 2-1 1.2c.6 1.3 1.5 2.2 2.8 2.8L7 6l2 2-1.2 1.3C4.5 9 1 5.5.7 2.2Z" fill="#4a9fd8"/></svg></li>
    <li>sales@tq-hr.example <svg viewBox="0 0 10 10"><rect x="0.5" y="2" width="9" height="6.5" fill="#4a9fd8"/><path d="M.5 2l4.5 3.5L9.5 2" stroke="#fff" stroke-width=".8" fill="none"/></svg></li>
    <li>7-8 Larkwell Meadow Trade Park, <svg viewBox="0 0 10 10"><circle cx="5" cy="3.5" r="2.5" fill="none" stroke="#4a9fd8" stroke-width="1.2"/><path d="M1.5 9.5c.5-2 2-3 3.5-3s3 1 3.5 3" fill="none" stroke="#4a9fd8" stroke-width="1.2"/></svg></li>
    <li style="padding-right:19px">Fennick Lane, United Kingdom</li>
  </ul>

  <div class="web-bar">www.tq-hr.example <svg viewBox="0 0 10 10"><circle cx="5" cy="5" r="4.2" fill="none" stroke="#fff"/><path d="M.8 5h8.4M5 .8c-2 2.5-2 5.9 0 8.4M5 .8c2 2.5 2 5.9 0 8.4" fill="none" stroke="#fff" stroke-width=".7"/></svg></div>
</section>

<section class="page page--inside">
  <svg class="page-art" viewBox="0 0 749 528" width="749" height="528">
    <defs>
      <linearGradient id="rail-tones" x1="0" y1="0" x2="1" y2="1">
        <stop offset="0" stop-color="#3d4a5c"/><stop offset=".35" stop-color="#f2d4a8"/><stop offset=".65" stop-color="#b9533f"/><stop offset="1" stop-color="#6d7885"/>
      </linearGradient>
      <linearGradient id="tinter-tones" x1="0" y1="0" x2="0" y2="1">
        <stop offset="0" stop-color="#d9d9d6"/><stop offset=".6" stop-color="#8e9196"/><stop offset="1" stop-color="#c9cbce"/>
      </linearGradient>
    </defs>
    <rect x="0" y="0" width="374" height="229" fill="url(#rail-tones)" role="img" aria-label="Photo: red high-speed train at a station platform at sunset"/>
    <rect x="17" y="212" width="118" height="37" fill="#1d3f95"/>
    <path d="M86,528 C180,470 330,420 355,318 C385,400 330,480 240,528 Z" fill="#5aaee0"/>
    <path d="M120,528 C215,480 335,430 355,322 C370,410 300,480 200,528 Z" fill="#1d3f95"/>
    <rect x="490" y="362" width="119" height="158" fill="url(#tinter-tones)" role="img" aria-label="Photo: automatic paint tinting machine with a coating bucket"/>
  </svg>

  <div class="products">
    <h2>Products:</h2>
    <ul>
      <li><svg viewBox="0 0 6 6"><path d="M.5 3l1.8 1.8L5.5 1" stroke="#1a1a1a" fill="none"/></svg>KVR 300 1K solvent free inorganic tintable finish coat for ultra UV durability</li>
      <li><svg viewBox="0 0 6 6"><path d="M.5 3l1.8 1.8L5.5 1" stroke="#1a1a1a" fill="none"/></svg>KVR 300 DM 1K solvent free clear coat for protection of steel and concrete substrates, anti graffiti, highly UV resistant</li>
      <li><svg viewBox="0 0 6 6"><path d="M.5 3l1.8 1.8L5.5 1" stroke="#1a1a1a" fill="none"/></svg>KVR BASEGUARD 2K epoxy hybrid anti corrosion coating for steel</li>
      <li><svg viewBox="0 0 6 6"><path d="M.5 3l1.8 1.8L5.5 1" stroke="#1a1a1a" fill="none"/></svg>KVR TILEMAX 1K glass flake single pack high abrasion resistant coating</li>
      <li><svg viewBox="0 0 6 6"><path d="M.5 3l1.8 1.8L5.5 1" stroke="#1a1a1a" fill="none"/></svg>KVR DURAMETAL 1K single component siloxane zinc anti-corrosion coating</li>
      <li><svg viewBox="0 0 6 6"><path d="M.5 3l1.8 1.8L5.5 1" stroke="#1a1a1a" fill="none"/></svg>KVR TANO 1K single component intermediate anti-corrosion coating</li>
      <li><svg viewBox="0 0 6 6"><path d="M.5 3l1.8 1.8L5.5 1" stroke="#1a1a1a" fill="none"/></svg>KVR 470 2K two component epoxy-siloxane hybrid durable tintable top coat</li>
      <li><svg viewBox="0 0 6 6"><path d="M.5 3l1.8 1.8L5.5 1" stroke="#1a1a1a" fill="none"/></svg>KVR DECKSHIELD 2K two component, chemical resistant, durable floor coating.</li>
      <li><svg viewBox="0 0 6 6"><path d="M.5 3l1.8 1.8L5.5 1" stroke="#1a1a1a" fill="none"/></svg>KVR STONEWEAR 2K two component ceramically filled epoxy for high abrasion resistance.</li>
    </ul>
  </div>

  <div class="spec spec--primers">
    <h3>1 and 2 Component Siloxane based Coatings:</h3>
    <table class="spec-table spec-table--primers">
      <colgroup><col class="col-product"><col class="col-comp"><col class="col-func"><col class="col-chem"><col class="col-dft"></colgroup>
      <thead><tr><th class="c-product">Product</th><th class="c-comp">Components</th><th class="c-func">Functionality</th><th class="c-chem">Chemistry</th><th class="c-dft">DFT (µm)</th></tr></thead>
      <tbody>
        <tr><td class="c-product">KVR TANO 1K</td><td class="c-comp">1</td><td class="c-func">Anti-corrosion Primer</td><td class="c-chem">Siloxane</td><td class="c-dft">150 - 200</td></tr>
        <tr><td class="c-product">KVR DURAMETAL 1K</td><td class="c-comp">1</td><td class="c-func">Anti-corrosion Primer</td><td class="c-chem">Siloxane-Zinc</td><td class="c-dft">75-100</td></tr>
        <tr><td class="c-product">KVR TILEMAX 1K</td><td class="c-comp">1</td><td class="c-func">Abrasion resistant Primer</td><td class="c-chem">Siloxane-Ceramic</td><td class="c-dft">200-250</td></tr>
        <tr><td class="c-product">KVR 300 1K</td><td class="c-comp">1</td><td class="c-func">Durable Topcoat</td><td class="c-chem">Siloxane</td><td class="c-dft">75-150</td></tr>
        <tr><td class="c-product">KVR 300 DM 1K</td><td class="c-comp">1</td><td class="c-func">Durable clear coat<br>(anti-graffiti)</td><td class="c-chem">Siloxane</td><td class="c-dft">25-50</td></tr>
        <tr><td class="c-product">KVR BASEGUARD 2K</td><td class="c-comp">2</td><td class="c-func">Anti-corrosion Primer</td><td class="c-chem">Epoxy-Hybrid</td><td class="c-dft">100 - 200</td></tr>
        <tr><td class="c-product">KVR STONEWEAR 2K</td><td class="c-comp">2</td><td class="c-func">Abrasion resistant Primer</td><td class="c-chem">Epoxy-Ceramic</td><td class="c-dft">200-250</td></tr>
        <tr><td class="c-product">KVR 470 2K</td><td class="c-comp">2</td><td class="c-func">Durable Topcoat</td><td class="c-chem">Siloxane-Hybrid</td><td class="c-dft">75-150</td></tr>
        <tr><td class="c-product">KVR DECKSHIELD 2K</td><td class="c-comp">2</td><td class="c-func">UV durable floor coating</td><td class="c-chem">Siloxane-hybrid</td><td class="c-dft">200-250</td></tr>
      </tbody>
    </table>
  </div>

  <div class="spec spec--topcoats">
    <h3>Tintable Top Coats:</h3>
    <table class="spec-table spec-table--topcoats">
      <colgroup><col class="col-product"><col class="col-comp"><col class="col-func"><col class="col-chem"><col class="col-dft"></colgroup>
      <thead><tr><th class="c-product">Product</th><th class="c-comp">Components</th><th class="c-func">Functionality</th><th class="c-chem">Chemistry</th><th class="c-dft">DFT (µm)</th></tr></thead>
      <tbody>
        <tr><td class="c-product">KVR 300 1K</td><td class="c-comp">1</td><td class="c-func">Durable Topcoat</td><td class="c-chem">RAL, BS &amp; Custom</td><td class="c-dft">75-150</td></tr>
        <tr><td class="c-product">KVR 470 2K</td><td class="c-comp">2</td><td class="c-func">Durable Topcoat</td><td class="c-chem">RAL, BS &amp; Custom</td><td class="c-dft">75-150</td></tr>
        <tr><td class="c-product">KVR DECKSHIELD 2K</td><td class="c-comp">2</td><td class="c-func">UV durable floor coating</td><td class="c-chem">RAL, BS &amp; Custom</td><td class="c-dft">200-250</td></tr>
      </tbody>
    </table>
  </div>
</section>

</body>
</html>
```